Edutainment company need help with Squarespace design

Need help completing website design for a hybrid education and entertainment company called "Quorvinabellis". The website will be based through Squarespace. A lot has been done, but need help to make look more consistent with branding and dynamic. Attached is brand kit already created by wonderful designer. Just want help keeping a professional look.

```html
<!DOCTYPE html>
<html lang="en">
<head>
<meta charset="UTF-8">
<title>Quorvinabellis — Where Learning Meets Entertainment</title>
<link rel="stylesheet" href="https://fonts.googleapis.com/css2?family=Luckiest+Guy&family=Montserrat:wght@400;500;600;700;800&display=swap">
<style>
  :root{
    --red:#d7321f;
    --red-dark:#b8261a;
    --ink:#111111;
    --text:#3b3b3b;
    --muted:#6b6b6b;
    --white:#ffffff;
    --yellow:#f9c21a;
    --yellow-deep:#f3a90d;
    --tan:#dca457;
    --pink:#e8386a;
    --teal:#1f9bc0;
    --footer:#161616;
    --line:#cfcfcf;
    --display:'Luckiest Guy', sans-serif;
    --body:'Montserrat', sans-serif;
  }
  *{box-sizing:border-box;margin:0;padding:0}
  html,body{width:1200px;height:4392px;overflow:hidden}
  body{font-family:var(--body);color:var(--text);background:var(--white);position:relative}
  .section{position:absolute;left:0;width:1200px}

  /* HERO */
  .hero{top:0;height:640px;background:linear-gradient(100deg,#5d6266 0%,#8e9396 45%,#b5b9bb 70%,#9fa4a7 100%);overflow:hidden}
  .hero-photo{position:absolute;right:0;top:0;width:520px;height:640px;background:radial-gradient(ellipse at 60% 45%,#c9a98e 0%,#8b7d72 35%,rgba(150,155,158,0) 70%)}
  .nav{position:absolute;top:0;left:0;width:1200px;height:120px}
  .brand{position:absolute;left:120px;top:28px;display:flex;align-items:center;gap:10px;font-family:var(--body);font-weight:800;font-size:26px;color:var(--white);letter-spacing:.5px}
  .brand-dot{width:22px;height:22px;border-radius:50%;background:var(--yellow)}
  .nav-links{position:absolute;left:520px;top:36px;display:flex;gap:28px;list-style:none;font-family:var(--display);font-size:16px;color:var(--white);letter-spacing:1px}
  .nav-links .active{color:var(--red)}
  .nav-cta{position:absolute;left:952px;top:22px;width:148px;height:44px;border-radius:22px;background:var(--red);color:var(--white);font-family:var(--display);font-size:15px;display:flex;align-items:center;justify-content:center;letter-spacing:1px}
  .hero-title{position:absolute;left:112px;top:176px;font-family:var(--display);font-size:56px;line-height:50px;color:var(--white);letter-spacing:2px;font-weight:400}
  .btn{display:inline-flex;align-items:center;justify-content:center;background:var(--red);color:var(--white);font-family:var(--display);font-size:14px;letter-spacing:1px;border-radius:22px}
  .hero .btn{position:absolute;left:112px;top:404px;width:170px;height:44px}
  .hero-arc{position:absolute;left:0;top:440px;width:1200px;height:140px}

  /* HEADINGS */
  .heading{font-family:var(--display);color:var(--ink);letter-spacing:2px;font-weight:400}
  .heading::after{content:"";display:block;width:70px;height:5px;background:var(--red);margin-top:12px}
  .heading.center{text-align:center}
  .heading.center::after{margin:12px auto 0}

  /* PROGRAMS */
  .programs{top:640px;height:560px}
  .programs .heading{position:absolute;left:112px;top:112px;font-size:42px}
  .cards{position:absolute;left:112px;top:200px;display:flex;gap:32px}
  .card{width:220px;height:262px;background:var(--white);box-shadow:0 6px 18px rgba(0,0,0,.16);padding:32px 24px}
  .card svg{width:56px;height:56px}
  .card h3{font-family:var(--display);font-size:17px;color:var(--ink);margin-top:22px;letter-spacing:.5px;font-weight:400}
  .card p{font-size:12px;line-height:17px;color:var(--muted);margin-top:10px}

  /* WHY */
  .why{top:1200px;height:972px;background:linear-gradient(160deg,var(--yellow) 0%,#fbd03a 50%,var(--yellow-deep) 100%);overflow:hidden}
  .why .heading{position:absolute;left:112px;top:116px;font-size:42px}
  .why-photo{position:absolute;right:0;bottom:0;width:560px;height:640px;background:radial-gradient(ellipse at 55% 60%,#8b5a3c 0%,#c58a4d 30%,rgba(249,194,26,0) 68%)}
  .blob{position:absolute;display:flex;align-items:center;justify-content:center;text-align:center;font-family:var(--display);font-size:24px;line-height:30px;color:var(--ink)}
  .blob svg{position:absolute;inset:0;width:100%;height:100%}
  .blob span{position:relative}
  .blob-tan{left:720px;top:176px;width:260px;height:210px}
  .blob-pink{left:176px;top:312px;width:290px;height:260px}
  .blob-teal{left:440px;top:696px;width:300px;height:200px}

  /* ABOUT */
  .about{top:2172px;height:548px}
  .about-photo{position:absolute;left:0;top:0;width:540px;height:548px;background:linear-gradient(135deg,#4f6fa8 0%,#c9885a 45%,#e8b35c 70%,#7a4c9a 100%)}
  .about .heading{position:absolute;left:600px;top:116px;font-size:42px}
  .about-copy{position:absolute;left:600px;top:196px;width:488px;font-size:15px;line-height:23px;color:var(--text)}
  .about-copy p+p{margin-top:20px}
  .about .btn{position:absolute;left:600px;top:468px;width:170px;height:44px}

  /* TESTIMONIALS */
  .testimonials{top:2720px;height:720px}
  .testimonials .heading{position:absolute;left:0;width:1200px;top:132px;font-size:42px}
  .quotes{position:absolute;left:128px;top:232px;display:flex;gap:60px}
  .quote{width:280px;text-align:center}
  .quote-photo{width:280px;height:240px;border-radius:10px}
  .q1{background:linear-gradient(135deg,#e88a1a,#c9602a)}
  .q2{background:linear-gradient(135deg,#3ec1e0,#1a8fb8)}
  .q3{background:linear-gradient(135deg,#d9d2c6,#8d7b66)}
  .quote h3{font-family:var(--display);font-size:18px;color:var(--ink);margin-top:32px;letter-spacing:.5px;font-weight:400}
  .quote p{font-size:13px;line-height:19px;color:var(--muted);margin:10px auto 0;width:230px}

  /* CONTACT */
  .contact{top:3440px;height:620px}
  .contact .heading{position:absolute;left:112px;top:60px;font-size:42px}
  .form{position:absolute;left:112px;top:138px;width:456px;font-size:12px;color:var(--ink);font-weight:500}
  .row{display:flex;gap:24px}
  .field{flex:1;margin-bottom:14px}
  .field label{display:block;margin-bottom:6px}
  .field .input{height:40px;border:1.5px solid var(--line);border-radius:20px}
  .field .area{height:124px;border:1.5px solid var(--line);border-radius:4px}
  .form .btn{width:178px;height:44px;margin-top:10px}
  .contact-photo{position:absolute;left:688px;top:72px;width:372px;height:468px}

  /* FOOTER */
  .footer{top:4060px;height:332px;background:var(--footer);color:var(--white)}
  .footer-brand{position:absolute;left:0;width:1200px;top:92px;display:flex;justify-content:center;align-items:center;gap:14px;font-weight:800;font-size:44px;letter-spacing:1px}
  .footer-brand .brand-dot{width:34px;height:34px}
  .footer-nav{position:absolute;top:260px;left:112px;display:flex;gap:24px;font-family:var(--display);font-size:15px;letter-spacing:1px}
  .footer-social{position:absolute;top:260px;left:592px;display:flex;gap:24px;font-family:var(--display);font-size:15px;letter-spacing:1px}
  .copyright{position:absolute;top:262px;left:844px;font-size:13px;color:#d8d8d8}
</style>
</head>
<body>

<section class="section hero">
  <div class="hero-photo" role="img" aria-label="Child wearing goggles and a lightbulb helmet, pointing upward"></div>
  <nav class="nav">
    <div class="brand"><span class="brand-dot"></span>Quorvinabellis</div>
    <ul class="nav-links">
      <li class="active">Home</li><li>About</li><li>Program</li><li>Testimonials</li>
    </ul>
    <div class="nav-cta">Contact Us</div>
  </nav>
  <h1 class="hero-title">Where<br>Learning<br>Meets<br>Entertainment</h1>
  <span class="btn">Book a Program</span>
  <svg class="hero-arc" viewBox="0 0 1200 140">
    <defs><path id="arc" d="M0 60 Q600 150 1200 10"/></defs>
    <text font-family="Luckiest Guy, sans-serif" font-size="20" fill="#ffffff">
      <textPath href="#arc" startOffset="8" textLength="1190" lengthAdjust="spacingAndGlyphs">WE BLEND EDUCATION WITH THE POWER OF ENTERTAINMENT TO INSPIRE, ENGAGE, AND CREATE</textPath>
    </text>
  </svg>
</section>

<section class="section programs">
  <h2 class="heading">Our Programs</h2>
  <div class="cards">
    <article class="card">
      <svg viewBox="0 0 56 56" fill="none" stroke="#111" stroke-width="2"><circle cx="28" cy="28" r="22"/><circle cx="28" cy="28" r="13"/><circle cx="28" cy="28" r="4"/><path d="M28 6v8M28 42v8M6 28h8M42 28h8"/></svg>
      <h3>Creative Learning</h3>
      <p>Hands-on lessons that spark curiosity, build skills and keep every young mind fully engaged.</p>
    </article>
    <article class="card">
      <svg viewBox="0 0 56 56" fill="none" stroke="#111" stroke-width="2"><rect x="6" y="6" width="44" height="30" rx="2"/><circle cx="18" cy="46" r="5"/><circle cx="38" cy="46" r="5"/><path d="M14 26l8-8 6 6 10-10"/></svg>
      <h3>Group Workshops</h3>
      <p>Team sessions where children play, explore and learn together through guided activities.</p>
    </article>
    <article class="card">
      <svg viewBox="0 0 56 56" fill="none" stroke="#111" stroke-width="2"><rect x="4" y="8" width="48" height="32" rx="2"/><path d="M18 48h20M28 40v8"/><circle cx="22" cy="24" r="6"/><path d="M34 18h10M34 26h10"/></svg>
      <h3>Digital Studio</h3>
      <p>Screen-based stories and games designed to teach new ideas in a fun, lasting way.</p>
    </article>
    <article class="card">
      <svg viewBox="0 0 56 56" fill="none" stroke="#111" stroke-width="2"><path d="M6 14h18a4 4 0 0 1 4 4v30a4 4 0 0 0-4-4H6z"/><path d="M50 14H32a4 4 0 0 0-4 4v30a4 4 0 0 1 4-4h18z"/><path d="M36 22h8M36 30h8"/></svg>
      <h3>Story Time</h3>
      <p>Reading adventures that grow language, imagination and confidence in every child.</p>
    </article>
  </div>
</section>

<section class="section why">
  <h2 class="heading">Why Quorvinabellis</h2>
  <div class="why-photo" role="img" aria-label="Smiling girl with curly hair spinning a desk globe"></div>
  <div class="blob blob-tan">
    <svg viewBox="0 0 260 210"><ellipse cx="130" cy="105" rx="130" ry="105" fill="#dca457"/></svg>
    <span>Learn<br>Through Play</span>
  </div>
  <div class="blob blob-pink">
    <svg viewBox="0 0 290 260"><path fill="#e8386a" d="M145 0l22 38 42-18 4 46 46 6-22 40 38 30-42 20 10 44-44-6-14 44-40-28-40 28-14-44-44 6 10-44-42-20 38-30-22-40 46-6 4-46 42 18z"/></svg>
    <span>Spark<br>Curiosity</span>
  </div>
  <div class="blob blob-teal">
    <svg viewBox="0 0 300 200"><path fill="#1f9bc0" d="M50 40a40 40 0 0 1 70-20a45 45 0 0 1 75 0a40 40 0 0 1 65 30a40 40 0 0 1 10 70a40 40 0 0 1-50 60a45 45 0 0 1-75 5a45 45 0 0 1-80-5a40 40 0 0 1-45-55a40 40 0 0 1 30-85z"/></svg>
    <span>Grow<br>Together</span>
  </div>
</section>

<section class="section about">
  <div class="about-photo" role="img" aria-label="Smiling boy painting at a classroom table"></div>
  <h2 class="heading">About Us</h2>
  <div class="about-copy">
    <p>We believe learning should feel like an adventure. Our team blends teaching with stage, screen and story so that children stay curious, laugh often and remember what they discover long after every session ends.</p>
    <p>From classrooms to community events, we design programs that mix play with purpose. Each activity is built by educators and performers working side by side to help young minds grow.</p>
  </div>
  <span class="btn">Book a Program</span>
</section>

<section class="section testimonials">
  <h2 class="heading center">Testimonials</h2>
  <div class="quotes">
    <figure class="quote">
      <div class="quote-photo q1" role="img" aria-label="Boy looking through a magnifying glass"></div>
      <h3>Happy Parent</h3>
      <p>My son now asks to learn every day. The sessions are fun and truly inspiring.</p>
    </figure>
    <figure class="quote">
      <div class="quote-photo q2" role="img" aria-label="Girl smiling with a thoughtful pose"></div>
      <h3>Proud Teacher</h3>
      <p>Our class loved every minute. Lessons stuck because they were so entertaining.</p>
    </figure>
    <figure class="quote">
      <div class="quote-photo q3" role="img" aria-label="Child writing at a desk"></div>
      <h3>Young Learner</h3>
      <p>It felt like a show and a lesson at once. I cannot wait for the next one.</p>
    </figure>
  </div>
</section>

<section class="section contact">
  <h2 class="heading">Let's Chat</h2>
  <div class="form">
    <div class="row">
      <div class="field"><label>Your Name *</label><div class="input"></div></div>
      <div class="field"><label>Your Name *</label><div class="input"></div></div>
    </div>
    <div class="field"><label>Email *</label><div class="input"></div></div>
    <div class="field"><label>Enter Your Message *</label><div class="area"></div></div>
    <span class="btn">Send Message</span>
  </div>
  <svg class="contact-photo" viewBox="0 0 372 468" role="img" aria-label="Two children wearing headphones using a laptop">
    <defs><linearGradient id="cg" x1="0" y1="0" x2="1" y2="1"><stop offset="0" stop-color="#3a6ea8"/><stop offset=".5" stop-color="#a0684a"/><stop offset="1" stop-color="#2c3f66"/></linearGradient></defs>
    <path fill="url(#cg)" d="M90 10c60-20 130-10 190 10c70 25 95 90 80 150c-12 45 10 90 2 140c-10 70-70 140-160 150c-80 8-150-30-180-90c-25-50 5-95-5-145C5 160 20 35 90 10z"/>
  </svg>
</section>

<footer class="section footer">
  <div class="footer-brand"><span class="brand-dot"></span>Quorvinabellis</div>
  <nav class="footer-nav"><span>Home</span><span>About</span><span>Program</span><span>Testimonials</span></nav>
  <nav class="footer-social"><span>Chatterbox</span><span>Friendhub</span></nav>
  <div class="copyright">Copyright ©2023. All Rights Reserved</div>
</footer>

</body>
</html>
```